Electrical panel service sticker w Bucket truck & Logo

We have a rather plain sticker we put on lighting panels to remind customers who to call for service. We want to redesign them with brushed aluminum background. We want a remake of the sticker with the outline of a bucket truck. You'll need to find or draw the outling of a bucket truck maybe with the boom up slightly as we will get these stickers die cut.

We want LOGO with Ph.# and Email.
Electrical * Lighting * Sign Service

Target Market(s)

Commercial property managers

Industry/Entity Type

Property Management

Requirements
Must have
• Bucket Truck Outline

```html
<!DOCTYPE html>
<html lang="en">
<head>
<meta charset="utf-8">
<title>Lumen Upkeep – Panel Service Sticker</title>
<link rel="stylesheet" href="https://fonts.googleapis.com/css2?family=Roboto+Condensed:wght@700&display=swap">
<style>
  :root {
    --plate-light: #f4f4f5;
    --plate-mid: #d9dadc;
    --plate-dark: #b9bbbe;
    --frame-navy: #121b33;
    --brand-red: #e32b32;
    --ink-navy: #0f1628;
    --ink-black: #111111;
    --art-tone: #c9cacc;
  }
  * { margin: 0; padding: 0; box-sizing: border-box; }
  html, body {
    width: 1200px;
    height: 900px;
    overflow: hidden;
    background: #ffffff;
  }
  .sticker {
    position: relative;
    width: 1200px;
    height: 900px;
    border-radius: 30px;
    background:
      repeating-linear-gradient(180deg, rgba(255,255,255,0.35) 0 1px, rgba(0,0,0,0.04) 1px 3px, rgba(255,255,255,0) 3px 5px),
      linear-gradient(100deg, var(--plate-dark) 0%, var(--plate-mid) 22%, var(--plate-light) 50%, var(--plate-mid) 78%, var(--plate-dark) 100%);
    font-family: "Roboto Condensed", "Arial Narrow", sans-serif;
  }
  .sticker__frame {
    position: absolute;
    left: 26px; top: 26px; right: 26px; bottom: 26px;
    border: 5px solid var(--frame-navy);
    border-radius: 24px;
  }
  .truck-art {
    position: absolute;
    left: 400px; top: 66px;
    width: 400px; height: 222px;
    border-radius: 10px;
    background: linear-gradient(180deg, var(--art-tone), #b3b4b7);
  }
  .brand-name {
    position: absolute;
    left: 0; right: 0; top: 296px;
    text-align: center;
    color: var(--brand-red);
    font-weight: 700;
    font-size: 142px;
    line-height: 138px;
    letter-spacing: 1px;
  }
  .phone {
    position: absolute;
    left: 0; right: 0; top: 618px;
    text-align: center;
    color: var(--ink-navy);
    font-weight: 700;
    font-size: 112px;
    line-height: 112px;
    letter-spacing: 1px;
  }
  .email, .services {
    position: absolute;
    left: 0; right: 0;
    text-align: center;
    color: var(--ink-black);
    font-weight: 700;
    font-size: 44px;
    line-height: 48px;
    text-transform: uppercase;
    letter-spacing: 1px;
  }
  .email { top: 728px; }
  .services { top: 788px; word-spacing: 4px; }
</style>
</head>
<body>
  <div class="sticker">
    <div class="sticker__frame"></div>
    <div class="truck-art" role="img" aria-label="Black line outline of a bucket truck with its boom raised, standing on a short ground line"></div>
    <h1 class="brand-name">Lumen<br>Upkeep</h1>
    <p class="phone">877-555-0142</p>
    <p class="email">service@lumenupkeep.com</p>
    <p class="services">Electrical • Lighting • Sign Service</p>
  </div>
</body>
</html>
```